Modified Business card

We have developed a new logo for the business, and want thou to tray and incorporate it into the business card design that you have done for us.

I am going to upload the logo files. We like the simple clean look that you have on the card, so if you can keep the look incorporating the logo.

Industry/Entity Type

Business

```html
<!DOCTYPE html>
<html lang="en">
<head>
<meta charset="utf-8">
<title>Halvern Engineering – Business Card</title>
<link rel="stylesheet" href="https://fonts.googleapis.com/css2?family=Open+Sans:wght@400;600;700&family=Oswald:wght@500&display=swap">
<style>
  :root {
    --page-bg: #2b2b2b;
    --card-bg: #f0f0f0;
    --band-grey: #d4d4d4;
    --accent-red: #e0283a;
    --text-dark: #2e2e2e;
    --text-grey: #666666;
    --brand-grey: #5c5c5c;
  }
  * { box-sizing: border-box; margin: 0; padding: 0; }
  html, body {
    width: 1200px; height: 1000px; overflow: hidden;
    background: var(--page-bg);
  }
  .canvas { position: relative; width: 1200px; height: 1000px; }

  .business-card {
    position: absolute; left: 150px; top: 243px;
    width: 900px; height: 514px;
    background: var(--card-bg);
    box-shadow: 0 18px 40px rgba(0,0,0,.45);
    overflow: hidden;
    font-family: "Open Sans", sans-serif;
  }
  .edge-band {
    position: absolute; left: 0; width: 100%; height: 24px;
    background: var(--band-grey);
  }
  .edge-band--top { top: 0; }
  .edge-band--bottom { bottom: 0; }
  .edge-tab {
    position: absolute; left: 243px; width: 387px; height: 30px;
    background: var(--accent-red);
  }
  .edge-tab--top { top: 0; border-radius: 0 0 14px 14px; }
  .edge-tab--bottom { bottom: 0; border-radius: 14px 14px 0 0; }

  .brand {
    position: absolute; left: 500px; top: 106px;
    display: flex; align-items: center; gap: 14px;
  }
  .brand__square {
    width: 58px; height: 58px; background: var(--accent-red); border-radius: 3px;
  }
  .brand__name {
    font-family: "Open Sans", sans-serif; font-weight: 600;
    font-size: 28px; color: var(--brand-grey); letter-spacing: .2px;
  }

  .holder { position: absolute; left: 82px; top: 255px; }
  .holder__name {
    font-family: "Oswald", sans-serif; font-weight: 500;
    font-size: 31px; line-height: 1; color: var(--text-grey);
    letter-spacing: -.3px;
  }
  .holder__role {
    margin-top: 4px; font-size: 15px; color: var(--accent-red);
  }

  .contact-list {
    position: absolute; left: 360px; top: 250px; list-style: none;
  }
  .contact-list__item {
    display: flex; align-items: flex-start; gap: 14px;
    height: 38px; font-size: 18px; line-height: 24px; color: var(--text-dark);
  }
  .contact-list__icon { width: 22px; height: 22px; flex: none; margin-top: 1px; }
  .contact-list__company { font-weight: 700; display: block; }
</style>
</head>
<body>
<main class="canvas">
  <section class="business-card" aria-label="Halvern Engineering business card">
    <div class="edge-band edge-band--top"></div>
    <div class="edge-band edge-band--bottom"></div>
    <div class="edge-tab edge-tab--top"></div>
    <div class="edge-tab edge-tab--bottom"></div>

    <div class="brand">
      <span class="brand__square"></span>
      <span class="brand__name">Halvern Engineering</span>
    </div>

    <div class="holder">
      <p class="holder__name">YOUR NAME</p>
      <p class="holder__role">General Manager</p>
    </div>

    <ul class="contact-list">
      <li class="contact-list__item">
        <svg class="contact-list__icon" viewBox="0 0 22 22"><circle cx="11" cy="11" r="10" fill="none" stroke="#2e2e2e" stroke-width="1.6"/><path d="M7.5 6.5l2 -0.5 1 2.5-1.2 1c.6 1.3 1.4 2.1 2.7 2.7l1-1.2 2.5 1-.5 2c-3.8.2-7.6-3.6-7.5-7.5z" fill="#2e2e2e"/></svg>
        <span>123 456 789</span>
      </li>
      <li class="contact-list__item">
        <svg class="contact-list__icon" viewBox="0 0 22 22"><circle cx="11" cy="11" r="10" fill="none" stroke="#2e2e2e" stroke-width="1.6"/><rect x="7.5" y="5.5" width="7" height="11" rx="1.2" fill="none" stroke="#2e2e2e" stroke-width="1.5"/><circle cx="11" cy="14.3" r=".9" fill="#2e2e2e"/></svg>
        <span>123 456 789</span>
      </li>
      <li class="contact-list__item">
        <svg class="contact-list__icon" viewBox="0 0 22 22"><circle cx="11" cy="11" r="10" fill="none" stroke="#2e2e2e" stroke-width="1.6"/><circle cx="11" cy="11" r="5.5" fill="none" stroke="#2e2e2e" stroke-width="1.3"/><path d="M5.5 11h11M11 5.5c-2.4 3-2.4 8 0 11M11 5.5c2.4 3 2.4 8 0 11" fill="none" stroke="#2e2e2e" stroke-width="1.1"/></svg>
        <span>www.yourwebsite.com</span>
      </li>
      <li class="contact-list__item">
        <svg class="contact-list__icon" viewBox="0 0 22 22"><circle cx="11" cy="11" r="10" fill="#2e2e2e"/><rect x="6" y="7.5" width="10" height="7" rx="1" fill="#f0f0f0"/><path d="M6.3 8l4.7 3.5L15.7 8" fill="none" stroke="#2e2e2e" stroke-width="1.1"/></svg>
        <span>info@yourcompany.com</span>
      </li>
      <li class="contact-list__item">
        <svg class="contact-list__icon" viewBox="0 0 22 22"><circle cx="11" cy="11" r="10" fill="none" stroke="#2e2e2e" stroke-width="1.6"/><path d="M11 16.5s-4-4.3-4-7a4 4 0 0 1 8 0c0 2.7-4 7-4 7z" fill="#2e2e2e"/><circle cx="11" cy="9.4" r="1.4" fill="#f0f0f0"/></svg>
        <span><span class="contact-list__company">Halvern Engineering</span>Address Company Location</span>
      </li>
    </ul>
  </section>
</main>
</body>
</html>
```